Create a memorable Stationary for Security Software Company

TalbrenQuay is the worldwide leader in securing the Internet. Making Internet communications and critical data secure, reliable and available everywhere has been and continues to be our ongoing vision. We are committed to staying focused on real customer needs and to developing new and innovative security solutions that redefine the security landscape.

Industry/Entity Type

Internet

Font styles to use
Serif
Sans Serif
Script

Colors
0792cd
33a6d7
85cae6

```html
<!DOCTYPE html>
<html lang="en">
<head>
<meta charset="utf-8">
<title>TalbrenQuay Stationery</title>
<link rel="stylesheet" href="https://fonts.googleapis.com/css2?family=Open+Sans:wght@400;600;700&display=swap">
<style>
  :root {
    --brand-deep: #0792cd;
    --brand-mid: #33a6d7;
    --brand-light: #85cae6;
    --paper-top: #1fb3dc;
    --ink-white: #ffffff;
    --window-line: #9aa3aa;
    --backdrop: #eef1f3;
    --ring: #3d4348;
    --face: linear-gradient(170deg, var(--paper-top) 0%, var(--brand-mid) 45%, var(--brand-deep) 100%);
  }
  * { box-sizing: border-box; margin: 0; padding: 0; }
  html, body { width: 1200px; height: 720px; overflow: hidden; }
  body { background: var(--backdrop); font-family: "Open Sans", Arial, sans-serif; color: var(--ink-white); }
  .canvas { position: relative; width: 1200px; height: 720px; }

  .piece { position: absolute; background: var(--face); box-shadow: 0 2px 6px rgba(0,0,0,.18); }

  .brand { display: flex; align-items: center; gap: 4px; font-weight: 600; color: var(--ink-white); white-space: nowrap; }
  .brand-dot { border-radius: 50%; background: var(--brand-light); flex: none; }

  /* Letterhead */
  .letterhead { left: 76px; top: 111px; width: 352px; height: 497px; }
  .letterhead .brand { position: absolute; left: 46px; top: 40px; font-size: 11px; }
  .letterhead .brand-dot { width: 14px; height: 14px; }
  .letter-body { position: absolute; left: 39px; top: 80px; width: 280px; font-size: 5.8px; line-height: 1.3; }
  .letter-body p { margin-bottom: 7px; }
  .letter-body h2 { font-size: 5.8px; font-weight: 400; }
  .letter-footer { position: absolute; left: 46px; bottom: 39px; font-size: 5.8px; }

  /* Business cards */
  .card { top: 109px; width: 150px; height: 84px; }
  .card-front { left: 460px; }
  .card-front .brand { position: absolute; left: 0; right: 0; top: 34px; justify-content: center; font-size: 9px; }
  .card-front .brand-dot { width: 10px; height: 10px; }
  .card-back { left: 651px; }
  .card-back .person { position: absolute; left: 10px; top: 11px; }
  .person-name { font-size: 8px; font-weight: 700; }
  .person-role { font-size: 4.5px; font-weight: 600; }
  .card-back .brand { position: absolute; right: 10px; top: 36px; font-size: 6px; }
  .card-back .brand-dot { width: 6px; height: 6px; }
  .contact { position: absolute; left: 10px; top: 54px; list-style: none; font-size: 4.6px; font-weight: 600; line-height: 1.5; }

  /* Envelopes */
  .envelope { width: 369px; height: 184px; }
  .envelope-front { left: 449px; top: 216px; }
  .envelope-front .brand { position: absolute; left: 24px; top: 52px; font-size: 11px; }
  .envelope-front .brand-dot { width: 12px; height: 12px; }
  .address-window { position: absolute; left: 186px; top: 78px; width: 150px; height: 74px; background: var(--ink-white); }
  .envelope-back { left: 448px; top: 421px; }
  .envelope-back svg { position: absolute; inset: 0; }

  /* Notepad */
  .notepad { left: 838px; top: 253px; width: 251px; height: 353px; }
  .notepad .brand { position: absolute; left: 0; right: 0; top: 140px; justify-content: center; font-size: 10px; }
  .notepad .brand-dot { width: 11px; height: 11px; }
  .spiral { position: absolute; left: 838px; top: 240px; }
</style>
</head>
<body>
<main class="canvas">

  <article class="piece letterhead">
    <div class="brand"><span class="brand-dot"></span>TalbrenQuay</div>
    <div class="letter-body">
      <p>TalbrenQuay builds security software that keeps internet communications and critical data safe, reliable and available everywhere. Our teams work with customers across the world to protect networks, devices and services, and we measure our progress by the trust our clients place in us every single day.</p>
      <h2>Network protection</h2>
      <p>Our gateways inspect traffic at scale, block threats before they reach users, and report clearly so teams can act fast without extra tools.</p>
      <h2>Data security</h2>
      <p>Encryption, key management and access control work together to keep records private at rest, in transit and in shared cloud storage.</p>
      <h2>Identity services</h2>
      <p>Single sign-on and strong authentication give every person the right access, with audits that stay simple for admins and clear for auditors.</p>
      <h2>Support worldwide</h2>
      <p>Engineers in every region answer quickly, day and night, and help customers plan, deploy and tune their security stack.</p>
    </div>
    <div class="letter-footer">talbrenquay.com/about</div>
  </article>

  <section class="piece card card-front">
    <div class="brand"><span class="brand-dot"></span>TalbrenQuay</div>
  </section>

  <section class="piece card card-back">
    <div class="person">
      <div class="person-name">Mara Quell</div>
      <div class="person-role">Co-Founder &amp; CEO</div>
    </div>
    <div class="brand"><span class="brand-dot"></span>TalbrenQuay</div>
    <ul class="contact">
      <li>T:&nbsp; (912) 555-0187</li>
      <li>M:&nbsp; mara@talbrenquay.com</li>
      <li>W:&nbsp; talbrenquay.com</li>
    </ul>
  </section>

  <section class="piece envelope envelope-front">
    <div class="brand"><span class="brand-dot"></span>TalbrenQuay</div>
    <div class="address-window">
      <svg width="150" height="74" viewBox="0 0 150 74">
        <g stroke="var(--window-line)" stroke-width="1">
          <line x1="17" y1="39" x2="133" y2="39"/>
          <line x1="17" y1="47" x2="133" y2="47"/>
          <line x1="17" y1="55" x2="133" y2="55"/>
          <line x1="17" y1="63" x2="133" y2="63"/>
        </g>
      </svg>
    </div>
  </section>

  <section class="piece envelope envelope-back">
    <svg width="369" height="184" viewBox="0 0 369 184">
      <path d="M4 0 V52 Q4 56 10 56 H359 Q365 56 365 52 V0" fill="none" stroke="rgba(0,60,100,.25)" stroke-width="1"/>
    </svg>
  </section>

  <section class="piece notepad">
    <div class="brand"><span class="brand-dot"></span>TalbrenQuay</div>
  </section>
  <svg class="spiral" width="251" height="30" viewBox="0 0 251 30">
    <g fill="none" stroke="var(--ring)" stroke-width="2">
      <ellipse cx="19" cy="15" rx="5" ry="11"/>
      <ellipse cx="44" cy="15" rx="5" ry="11"/>
      <ellipse cx="69" cy="15" rx="5" ry="11"/>
      <ellipse cx="94" cy="15" rx="5" ry="11"/>
      <ellipse cx="119" cy="15" rx="5" ry="11"/>
      <ellipse cx="144" cy="15" rx="5" ry="11"/>
      <ellipse cx="169" cy="15" rx="5" ry="11"/>
      <ellipse cx="194" cy="15" rx="5" ry="11"/>
      <ellipse cx="219" cy="15" rx="5" ry="11"/>
      <ellipse cx="240" cy="15" rx="5" ry="11"/>
    </g>
  </svg>

</main>
</body>
</html>
```